■ 依頼の目的/概要

私は第45回全国青葉学徒競技祭典選手権(以下、葉徒祭)運営委員会の広報局長を務めております。葉徒祭というのは、東日本と西日本から選抜された医学部学生が参加する体育大会で、開催競技は全12競技となっております。

今回は、その大会のPR用に各大学に配布するポスターのデザイン制作をお願いします。

■ 重視する点/検討基準

ポスターを見るのは主に大学医学部の学生で、一目見て葉徒祭のポスターだと分かるものがいいです。

制作する上で、必ず入れてほしいワードを以下に述べておきます。

・第45回全国青葉学徒競技祭典選手権
http://www.hatosai.kumonet.jp/top.htm(※大会HPです)
・主管:白鷺ヶ丘医療学院・浜風医療学院
・主催:北辰学徒競技協会連合・南星学徒競技協会連合
・開催競技(弓道・硬式テニス・軟式テニス・バトミントン・準硬式野球・サッカー・バスケットボール・柔道・卓球・剣道・バレーボール・ヨットの全12競技)

前年度、前々年度のポスターを添付しておりますので、ご参照下さい。

■ 利用用途

A2サイズのポスターに、片面カラーで印刷します。また、大会HPにも掲載いたします。

■ その他/注意点

データはイラストレーター形式(CS3以下)にて縦長使用でお願いします。
そのまま印刷会社に入稿するので、カラーモードはCMYKにて、塗り足し・アウトライン化もお願いします。

・ご提案を選択後に当選者様に修正を依頼する可能性がございますのでご了承下さい。
・選択させて頂いたデザインの著作権(財産権)等の扱いはMokkaro利用規約に従い、弊運営委員会に譲渡をお願いします。フォントや画像素材などを利用する場合は上記利用用途に使用できることを確認し、第三者の知的財産権等に注意して下さい。

葉徒祭につきましては下記のサイトをご参照下さい。何らかのご参考にしていただけると幸いです。また、第45回の大会HPはまだ制作しておりません。
http://www.hatosai.kumonet.jp/top.htm
http://ja.hyakkamori.jp/wiki/%E8%91%89%E5%BE%92%E7%A5%AD

以上、宜しくお願い致します。

たくさんのデザイン提案、どうもありがとうございます。
私1人だけでなく、実行委員何人かで最も相応しいと思われるものを選ばせて頂きたいと思います。
二週間位内には選びたいと思います。
■ 選んだ理由

医学生の部屋に貼っているイメージとの提案で、それが私たちのイメージにぴったりでした。また、大学に貼っていても目を引きそうなデザインでとても気に入りました。

■ 提案者全員のお礼・コメント

たくさんの提案ありがとうございました。
すばらしいものばかりだったので選ぶのに迷いましたが、委員何人かで話し合い今回はこのデザインを選ばせていただくことにしました。

```html
<!DOCTYPE html>
<html lang="ja">
<head>
<meta charset="utf-8">
<title>第45回 全国青葉学徒競技祭典選手権</title>
<link href="https://fonts.googleapis.com/css2?family=Noto+Sans+JP:wght@700;900&family=Oswald:wght@600&display=swap" rel="stylesheet">
<style>
  :root {
    --navy: #1e3290;
    --navy-deep: #14216b;
    --white: #ffffff;
    --yellow: #f6e500;
    --shadow: rgba(8, 16, 60, .55);
  }
  * { margin: 0; padding: 0; box-sizing: border-box; }
  html, body { width: 849px; height: 1200px; overflow: hidden; background: var(--navy-deep); }
  .poster {
    position: relative;
    width: 849px;
    height: 1200px;
    overflow: hidden;
    background: radial-gradient(ellipse at 40% 40%, var(--navy) 0%, var(--navy-deep) 100%);
    font-family: "Noto Sans JP", sans-serif;
    color: var(--white);
  }
  .chalk-doodles {
    position: absolute;
    inset: 0;
    background:
      radial-gradient(ellipse 260px 120px at 230px 230px, rgba(143,200,239,.22), transparent 70%),
      radial-gradient(ellipse 300px 140px at 330px 560px, rgba(143,200,239,.18), transparent 70%),
      radial-gradient(ellipse 240px 110px at 520px 840px, rgba(143,200,239,.18), transparent 70%),
      radial-gradient(ellipse 200px 90px at 160px 980px, rgba(143,200,239,.14), transparent 70%);
  }
  .title { font-weight: 900; }
  .edition {
    position: absolute;
    left: 150px;
    top: 38px;
    padding: 4px 18px;
    background: var(--yellow);
    color: var(--navy-deep);
    font-size: 36px;
    line-height: 1.1;
    transform: rotate(-10deg);
  }
  .title-line {
    position: absolute;
    left: 34px;
    display: block;
    line-height: 1;
    letter-spacing: -2px;
    white-space: nowrap;
    transform: rotate(-6deg) skewX(-6deg);
    transform-origin: left bottom;
    text-shadow: 5px 5px 0 var(--shadow);
  }
  .line-1 { top: 110px; font-size: 175px; }
  .line-2 { top: 300px; font-size: 152px; }
  .line-3 { top: 500px; font-size: 178px; }
  .line-4 { top: 720px; font-size: 205px; }
  .accent { color: var(--yellow); }
  .events {
    position: absolute;
    top: 28px;
    right: 22px;
    list-style: none;
    font-weight: 700;
    font-size: 19px;
    line-height: 1.58;
  }
  .site-url {
    position: absolute;
    left: 30px;
    top: 1040px;
    transform: rotate(-7deg);
    transform-origin: left top;
    font-family: "Oswald", sans-serif;
    font-weight: 600;
    font-size: 34px;
    color: var(--yellow);
    letter-spacing: .5px;
    white-space: nowrap;
  }
  .credits {
    position: absolute;
    right: 22px;
    bottom: 26px;
    font-size: 14px;
    font-weight: 700;
    line-height: 1;
  }
  .credit-row { display: flex; align-items: center; gap: 8px; margin-top: 9px; }
  .credit-label {
    background: var(--white);
    color: var(--navy-deep);
    padding: 3px 6px;
    font-size: 13px;
  }
</style>
</head>
<body>
<main class="poster">
  <div class="chalk-doodles" role="img" aria-label="青いチョークの落書きと手描きの線"></div>

  <h1 class="title">
    <span class="edition">第45回</span>
    <span class="title-line line-1">全国</span>
    <span class="title-line line-2">青葉<span class="accent">学徒</span></span>
    <span class="title-line line-3">競技祭典</span>
    <span class="title-line line-4"><span class="accent">選手</span>権</span>
  </h1>

  <ul class="events">
    <li>バスケットボール</li>
    <li>バレーボール</li>
    <li>硬式テニス</li>
    <li>軟式テニス</li>
    <li>バトミントン</li>
    <li>準硬式野球</li>
    <li>サッカー</li>
    <li>柔道</li>
    <li>卓球</li>
    <li>剣道</li>
    <li>弓道</li>
    <li>ヨット</li>
  </ul>

  <p class="site-url">http://www.hatosai.kumonet.jp/top.htm</p>

  <div class="credits">
    <p class="credit-row"><span class="credit-label">主管</span>白鷺ヶ丘医療学院・浜風医療学院</p>
    <p class="credit-row"><span class="credit-label">主催</span>北辰学徒競技協会連合・南星学徒競技協会連合</p>
  </div>
</main>
</body>
</html>
```